Email signature design - law firm

We are a small boutique law firm which is located near the beach in Manly, Australia.

We have just recently developed a new logo and are looking to redesign our letterhead, business cards and email signatures.

This brief is for our email signatures. This is an email signature to appear at the bottom of our Outlook emails so we would like it to be text that we are able to edit as the wording in our email signature often required amendments.

I have attached a word document which had our new logo, and our previous email signature which all the information/wording that needs to be included.

We would like multiple designs with a modern, simplistic yet striking look.

Thanks.

font - raleway or montserrat
Updates

Colors

Designer to choose colors to be used in the design.

Requirements
Must have
• Must have the exact wording which appears in the email signature in the word document attached to brief.
• Must be able to edit the text as it is for an Outlook email signature which wording will change from time to time.

```html
<!DOCTYPE html>
<html lang="en">
<head>
<meta charset="utf-8">
<title>Email Signature – Harwell &amp; Partners</title>
<link rel="stylesheet" href="https://fonts.googleapis.com/css2?family=Montserrat:wght@500;600&display=swap">
<style>
  :root {
    --ink: #111111;
    --navy: #3a4590;
    --paper: #ffffff;
  }
  * { margin: 0; padding: 0; box-sizing: border-box; }
  html, body {
    width: 1200px;
    height: 938px;
    overflow: hidden;
    background: var(--paper);
  }
  .signature {
    position: relative;
    width: 1200px;
    height: 938px;
    padding: 153px 0 0 49px;
    font-family: "Montserrat", Arial, sans-serif;
    font-weight: 500;
    color: var(--ink);
  }
  .sign-off { font-size: 16.5px; line-height: 22px; }
  .person-name {
    margin-top: 14px;
    font-size: 19.5px;
    font-weight: 600;
    color: var(--navy);
    line-height: 24px;
  }
  .firm-name {
    margin-top: 9px;
    font-size: 16.5px;
    font-weight: 600;
    color: var(--navy);
    line-height: 20px;
  }
  .address { font-size: 15.5px; line-height: 18.5px; }
  .address .spaced { word-spacing: 18px; }
  .contact { margin-top: 11px; font-size: 15.5px; line-height: 22.5px; }
  .contact .label { color: var(--navy); }
  .firm-mark {
    margin-top: 34px;
    display: flex;
    align-items: center;
    gap: 10px;
    height: 70px;
    font-size: 17px;
    font-weight: 600;
    color: var(--navy);
  }
  .firm-mark .dot {
    width: 26px; height: 26px;
    border-radius: 50%;
    background: var(--navy);
  }
  .notices {
    position: absolute;
    left: 49px;
    top: 538px;
    width: 1120px;
    font-size: 14.8px;
    line-height: 16.8px;
  }
  .notices p { margin-bottom: 17px; }
  .notices p.fraud { margin-top: 33px; }
</style>
</head>
<body>
  <div class="signature">
    <p class="sign-off">Regards,</p>
    <p class="person-name">Nadia Fairweather</p>
    <p class="firm-name">Harwell &amp; Partners</p>
    <p class="address">Suite 4, 27 Tidewater Lane<br><span class="spaced">SEACLIFF NSW 2090</span></p>
    <p class="contact">
      <span class="label">Ph:</span> (02) 9000 1234<br>
      <span class="label">Fax:</span> (02) 9000 1235<br>
      www.harwellpartners.com.au
    </p>
    <div class="firm-mark">
      <span class="dot"></span>
      <span>Harwell &amp; Partners</span>
    </div>

    <div class="notices">
      <p>Important note: This E-Mail and any attachment is PRIVILEGED and confidential.&nbsp; It must not be read, copied, disclosed or used by any person other than the above named addressees.&nbsp; In order to preserve the intended confidentiality and privilege, please notify us immediately if you have received this e-mail by mistake and secure-delete this e-mail from your system.</p>
      <p>Unauthorised perusal, use, disclosure, forwarding or copying is strictly prohibited and may be unlawful.</p>
      <p>Liability limited by a scheme approved under Professional Standards Legislation. Legal practitioners at Harwell Legal (NSW) Pty Ltd are members of the scheme.</p>
      <p class="fraud">Fraud warning: Please be aware that there is a significant risk posed by cyber fraud, specifically relating to email accounts and bank account details. Our bank account details will never change during the course of a transaction, and we will never advise you of a change to our bank details via email.&nbsp; Please check account details with us in person or by phone before making payments.&nbsp; If you advise us of your bank account details by email, please also ring and confirm the bank account details by phone as well.</p>
    </div>
  </div>
</body>
</html>
```